Business Card Design

Consultation for design, construction athletic facilities specializing in synthetic turf systems and all weather running track systems.
Motto "True Owner Representation"
New Company that we'd like to highlight the LOGO first and foremost with the colors of the background and font as primary colors of the card too if possible. I've also attached a typical larger project design layout that could be used in the background to highlight our design and construction specialty.
Website is something we want very noticeable for driving traffic.
Target Market(s)
Athletic Directors, Designers, Government and Military, Contractors
Industry/Entity Type
Construction
Contact Information for Business Card
Peter L. Vandrell CFB, CTB
48317 W 63rd Ave
Harlow Ridge, WA 99482
C +1 503.555.0147
O +1 808.555.0182
Peter@fieldlaneco.example
www.fieldlaneco.example

```html
<!DOCTYPE html>
<html lang="en">
<head>
<meta charset="utf-8">
<title>Kestra Field – Business Card</title>
<link href="https://fonts.googleapis.com/css2?family=Arimo:wght@400;700&display=swap" rel="stylesheet">
<style>
  :root {
    --bg: #e9e6e1;
    --card-black: #060606;
    --gold-deep: #d9a514;
    --gold-mid: #f0c93a;
    --gold-pale: #fbf4dc;
    --ink: #141414;
    --logo: #d9b36a;
    --motto: #e8b21c;
    --rule: rgba(120, 90, 20, 0.35);
  }
  * { box-sizing: border-box; margin: 0; padding: 0; }
  html, body { width: 1200px; height: 858px; overflow: hidden; }
  body {
    background: var(--bg);
    font-family: "Arimo", Arial, sans-serif;
    display: flex;
    align-items: center;
    justify-content: center;
    gap: 48px;
  }
  .card {
    width: 540px;
    height: 308px;
    background: var(--card-black);
    position: relative;
    overflow: hidden;
    box-shadow: 0 10px 26px rgba(0,0,0,0.25);
  }
  .gold-band {
    position: absolute;
    left: 0; right: 0;
    background: linear-gradient(90deg, var(--gold-deep) 0%, var(--gold-mid) 22%, var(--gold-pale) 50%, var(--gold-mid) 78%, var(--gold-deep) 100%);
  }

  /* Front */
  .card-front .logo-area {
    position: absolute;
    top: 0; left: 0; right: 0;
    height: 168px;
    display: flex;
    align-items: center;
    justify-content: center;
    gap: 18px;
  }
  .logo-dot {
    width: 34px; height: 34px;
    border-radius: 50%;
    background: var(--logo);
  }
  .logo-name {
    color: var(--logo);
    font-weight: 400;
    font-size: 38px;
    letter-spacing: 0.18em;
  }
  .card-front .gold-band {
    bottom: 0;
    height: 140px;
    display: flex;
  }
  .person {
    flex: 1;
    padding: 24px 22px 0 16px;
    text-align: right;
    color: var(--ink);
    border-right: 1px solid var(--rule);
    margin: 14px 0;
  }
  .person-name { font-size: 22px; font-weight: 400; }
  .person-title { font-size: 14px; margin: 3px 0 8px; }
  .person-address { font-size: 12.5px; line-height: 1.45; }
  .contacts {
    flex: 1;
    list-style: none;
    padding: 30px 0 0 22px;
    color: var(--ink);
    font-size: 13px;
  }
  .contacts li {
    display: flex;
    align-items: center;
    gap: 9px;
    height: 21px;
  }
  .contacts svg { width: 13px; height: 13px; flex: none; }

  /* Back */
  .card-back .logo-area {
    position: absolute;
    top: 0; left: 0; right: 0;
    height: 246px;
    display: flex;
    flex-direction: column;
    align-items: center;
    justify-content: center;
    gap: 12px;
  }
  .card-back .logo-row { display: flex; align-items: center; gap: 20px; }
  .card-back .logo-name { font-size: 46px; }
  .motto {
    color: var(--motto);
    font-size: 17px;
    letter-spacing: 0.02em;
  }
  .card-back .gold-band {
    bottom: 0;
    height: 62px;
    display: flex;
    align-items: center;
    justify-content: center;
  }
  .website {
    color: var(--ink);
    font-size: 26px;
    letter-spacing: 0.01em;
  }
</style>
</head>
<body>

<section class="card card-front" aria-label="Business card front">
  <div class="logo-area">
    <span class="logo-dot"></span>
    <span class="logo-name">KESTRA field</span>
  </div>
  <div class="gold-band">
    <div class="person">
      <p class="person-name">Peter L. Vandrell</p>
      <p class="person-title">CFB, CTB</p>
      <p class="person-address">48317 W 63rd Ave<br>Harlow Ridge, WA 99482</p>
    </div>
    <ul class="contacts">
      <li>
        <svg viewBox="0 0 16 16"><rect x="4" y="1" width="8" height="14" rx="1.5" fill="none" stroke="#141414" stroke-width="1.6"/><circle cx="8" cy="12.5" r="0.9" fill="#141414"/></svg>
        +1 503.555.0147
      </li>
      <li>
        <svg viewBox="0 0 16 16"><path d="M2 6c0-2 2-3 6-3s6 1 6 3v1h-3V5.5H5V7H2z" fill="#141414"/><rect x="3" y="8" width="10" height="6" rx="1" fill="#141414"/></svg>
        +1 808.555.0182
      </li>
      <li>
        <svg viewBox="0 0 16 16"><rect x="1.5" y="3.5" width="13" height="9" fill="none" stroke="#141414" stroke-width="1.5"/><path d="M1.5 3.5 8 9l6.5-5.5" fill="none" stroke="#141414" stroke-width="1.5"/></svg>
        Peter@fieldlaneco.example
      </li>
      <li>
        <svg viewBox="0 0 16 16"><circle cx="8" cy="8" r="6.5" fill="none" stroke="#141414" stroke-width="1.4"/><ellipse cx="8" cy="8" rx="2.8" ry="6.5" fill="none" stroke="#141414" stroke-width="1.2"/><path d="M1.5 8h13" stroke="#141414" stroke-width="1.2"/></svg>
        www.fieldlaneco.example
      </li>
    </ul>
  </div>
</section>

<section class="card card-back" aria-label="Business card back">
  <div class="logo-area">
    <div class="logo-row">
      <span class="logo-dot"></span>
      <span class="logo-name">KESTRA field</span>
    </div>
    <p class="motto">True Owner Representation</p>
  </div>
  <div class="gold-band">
    <p class="website">www.fieldlaneco.example</p>
  </div>
</section>

</body>
</html>
```